Loyalty/Gift Card Design-

Pumlavo needs a design for a loyalty card for a retail gas discount program. The card will need to fit specifications for brenvoxa cards cr-80 magnetic card found on www.brenvoxa.com

The way our program works is a consumer will see advertisement for our program and come to a local gas station to purchase our Pumlavo Card. It will be a set price up- front, then our program/card will save consumers 15 cents per gallon on 100 gallons of fuel. Once the 100 gallons is used the customer will have the option of reloading (for another set cost) another 100 gallons on the card to receive another 15 cents off on next 100 gallons.

Key Info to Incorporate on card--
"Save 15 cents per gallon on next 100 gallons of fuel"
Never pay full price on fuel again!
"Card Valid Only At" (then a space for our stores name and address)
Brought to you by-- Pumlavo Name & Logo

Target Market(s)

Consumers conscious of gas prices/ economy who are looking to save money where they can. We are looking for a design that fits "big box" theme, with very clean design.

Industry/Entity Type

Gas Station

Requirements
Must have
• Colors Red,, Blue, White--
Sell Message of Saving and Value.
Should not have
• Designs with fuel pumps

```html
<!DOCTYPE html>
<html lang="en">
<head>
<meta charset="utf-8">
<title>Pumlavo Fuel Card</title>
<link href="https://fonts.googleapis.com/css2?family=Asap:wght@300;400;600;700;800&display=swap" rel="stylesheet">
<style>
  :root {
    --page: #ffffff;
    --card-red: #c9161f;
    --card-red-deep: #a80f17;
    --card-red-light: #dc1f27;
    --brand-blue: #1c3f9e;
    --brand-blue-bright: #1f6fd0;
    --silver: #e9eaec;
    --silver-light: #fbfbfb;
    --stripe: #231f20;
    --ink: #1e1e1e;
    --white: #ffffff;
  }
  * { margin: 0; padding: 0; box-sizing: border-box; }
  html, body {
    width: 1180px;
    height: 1200px;
    overflow: hidden;
    background: var(--page);
    font-family: "Asap", Arial, sans-serif;
  }
  .sheet { position: relative; width: 1180px; height: 1200px; }
  .card {
    position: absolute;
    left: 234px;
    width: 712px;
    height: 459px;
    overflow: hidden;
    border: 1px solid #555;
  }
  .card--front { top: 114px; background: linear-gradient(160deg, var(--silver-light), var(--silver)); }
  .card--back { top: 627px; background: radial-gradient(ellipse at 30% 20%, var(--card-red-light), var(--card-red) 55%, var(--card-red-deep)); }
  .card__wave { position: absolute; inset: 0; width: 100%; height: 100%; }
  .card__frame {
    position: absolute;
    inset: 14px 18px 14px 18px;
    border: 1.5px solid rgba(255,255,255,0.85);
    border-radius: 16px;
  }
  .card--back .card__frame { inset: 14px 16px 14px 20px; border-radius: 22px; }
  .offer {
    position: absolute;
    left: 58px;
    top: 4px;
    color: var(--brand-blue);
    line-height: 1;
  }
  .offer__amount {
    display: block;
    font-size: 176px;
    font-weight: 800;
    letter-spacing: -6px;
  }
  .offer__cent { font-size: 80px; vertical-align: 62px; letter-spacing: 0; margin-left: 4px; }
  .offer__unit {
    display: block;
    font-size: 43px;
    font-weight: 700;
    margin-top: -22px;
    margin-left: 0;
  }
  .brand {
    position: absolute;
    left: 344px;
    top: 50px;
    display: flex;
    align-items: center;
    gap: 14px;
  }
  .brand__mark { width: 48px; height: 48px; background: var(--brand-blue); }
  .brand__name { font-size: 52px; font-weight: 700; color: var(--brand-blue); }
  .card-number {
    position: absolute;
    left: 88px;
    top: 240px;
    font-size: 47px;
    font-weight: 300;
    color: var(--ink);
    word-spacing: 16px;
    letter-spacing: 1px;
  }
  .promo {
    position: absolute;
    left: 51px;
    top: 359px;
    color: var(--white);
    font-size: 25px;
    font-weight: 700;
    line-height: 1.3;
  }
  .mag-stripe {
    position: absolute;
    left: 0; right: 0;
    top: 54px;
    height: 101px;
    background: var(--stripe);
  }
  .store-info {
    position: absolute;
    left: 67px;
    top: 244px;
    color: var(--white);
    font-size: 24px;
    font-weight: 700;
    line-height: 54px;
  }
</style>
</head>
<body>
<main class="sheet">
  <section class="card card--front" aria-label="Card front">
    <svg class="card__wave" viewBox="0 0 712 459" preserveAspectRatio="none" aria-hidden="true">
      <defs>
        <linearGradient id="redFill" x1="0" y1="0" x2="1" y2="1">
          <stop offset="0" stop-color="#d81d26"/>
          <stop offset="1" stop-color="#b3111a"/>
        </linearGradient>
        <linearGradient id="blueFill" x1="0" y1="0" x2="1" y2="0">
          <stop offset="0" stop-color="#1c3f9e"/>
          <stop offset="0.6" stop-color="#1a4bb4"/>
          <stop offset="1" stop-color="#1f7ad8"/>
        </linearGradient>
      </defs>
      <path d="M0 186 C120 196 220 238 330 238 C450 238 560 150 712 156 L712 459 L0 459 Z" fill="url(#blueFill)"/>
      <path d="M0 204 C120 214 220 256 335 254 C460 252 570 170 712 176 L712 459 L0 459 Z" fill="url(#redFill)"/>
    </svg>
    <div class="card__frame"></div>
    <div class="offer">
      <span class="offer__amount">15<span class="offer__cent">¢</span></span>
      <span class="offer__unit">Per Gallon</span>
    </div>
    <div class="brand">
      <span class="brand__mark"></span>
      <span class="brand__name">Pumlavo</span>
    </div>
    <p class="card-number">0000 0000 0000 0000</p>
    <p class="promo">Save 15 cents per gallon on next 100 gallons of fuel<br>Never pay full price on fuel again!</p>
  </section>

  <section class="card card--back" aria-label="Card back">
    <div class="card__frame"></div>
    <div class="mag-stripe"></div>
    <div class="store-info">
      <p>Card Valid Only At</p>
      <p>Address :</p>
    </div>
  </section>
</main>
</body>
</html>
```